Business Card Design - Corporate

Create a sleek elegant business card layout while suggesting a color scheme. Convey cutting edge technology while maintaining a corporate feel that is easily readable.

Company designs and manufactures consumer electronic products for mass retail that are mainly app driven.

(vector logo and die-line provided)

Target Market(s)

Corporate level, tech industry.

Industry/Entity Type

Business

Contact Information for Business Card

Generic Info:

Name
Title
email
address
phone 1
phone 2
website (quillbarn.com) on back

Font styles to use
Sans Serif

Requirements
Must have
• At least 2 colors + white on one side.
Nice to have
• Solid suggestion on color for logo and overall design. Color flood on back of card.
Should not have
• background texture like... marble, stone, patterns or circuit boards

```html
<!DOCTYPE html>
<html lang="en">
<head>
<meta charset="utf-8">
<title>Quillbarn Business Card</title>
<link href="https://fonts.googleapis.com/css2?family=Open+Sans:wght@400;600;700&display=swap" rel="stylesheet">
<style>
  :root {
    --backdrop: #2b2b2b;
    --card: #ffffff;
    --ink: #555555;
    --ink-dark: #3f3f3f;
    --band: #5a5a5a;
    --accent: #1a6fbd;
  }
  * { box-sizing: border-box; margin: 0; padding: 0; }
  html, body {
    width: 1200px; height: 1000px; overflow: hidden;
    background: var(--backdrop);
    font-family: "Open Sans", Arial, sans-serif;
  }
  .card {
    position: absolute; left: 280px;
    width: 640px; height: 366px;
    background: var(--card);
    overflow: hidden;
  }
  .card--front { top: 104px; }
  .card--back { top: 530px; }

  .wordmark {
    font-weight: 600; color: var(--ink);
    letter-spacing: 0.14em; text-transform: uppercase;
    line-height: 1; white-space: nowrap;
  }
  .card--front .wordmark {
    position: absolute; left: 0; right: 0; top: 142px;
    text-align: center; font-size: 58px;
  }
  .front-url {
    position: absolute; left: 0; right: 0; top: 218px;
    text-align: center; font-size: 15px; font-weight: 600;
    color: var(--ink); letter-spacing: 0.08em;
  }

  .card--back .wordmark {
    position: absolute; left: 46px; top: 74px; font-size: 40px;
  }
  .person {
    position: absolute; right: 40px; top: 66px; width: 200px;
    text-align: center;
  }
  .person__badge { display: block; margin: 0 auto 4px; }
  .person__name { color: var(--accent); font-size: 25px; font-weight: 700; line-height: 1.15; }
  .person__title { color: var(--ink-dark); font-size: 17px; font-weight: 600; line-height: 1.3; }

  .band {
    position: absolute; left: 0; right: 0; top: 180px; height: 72px;
    background: var(--band);
  }
  .contact {
    position: absolute; top: 192px; width: 210px;
    text-align: center; color: var(--ink); font-size: 16px; line-height: 1.35;
  }
  .contact--phone { left: 2px; }
  .contact--web { left: 215px; }
  .contact--place { left: 428px; }
  .contact__icon { display: block; margin: 0 auto 12px; }
  .contact a { color: inherit; text-decoration: none; }
  .contact .domain { color: var(--accent); }
  .stripe {
    position: absolute; left: 0; right: 0; bottom: 0; height: 14px;
    background: var(--accent);
  }
</style>
</head>
<body>

<section class="card card--front" aria-label="Card front">
  <div class="wordmark">Quillbarn</div>
  <div class="front-url">www.quillbarn.com</div>
</section>

<section class="card card--back" aria-label="Card back">
  <div class="wordmark">Quillbarn</div>

  <div class="person">
    <svg class="person__badge" width="38" height="38" viewBox="0 0 38 38" aria-hidden="true">
      <circle cx="19" cy="19" r="19" fill="var(--accent)"/>
    </svg>
    <div class="person__name">Dana Kerr</div>
    <div class="person__title">President</div>
  </div>

  <div class="band"></div>

  <div class="contact contact--phone">
    <svg class="contact__icon" width="40" height="72" viewBox="0 0 40 72" aria-hidden="true">
      <path d="M11 60 L20 72 L29 60Z" fill="var(--band)"/>
      <circle cx="20" cy="20" r="18" fill="var(--accent)"/>
      <rect x="14" y="9" width="12" height="21" rx="2" fill="none" stroke="#fff" stroke-width="2"/>
      <circle cx="20" cy="26.5" r="1.2" fill="#fff"/>
    </svg>
    000 000 0000<br>000 000 0000
  </div>

  <div class="contact contact--web">
    <svg class="contact__icon" width="40" height="72" viewBox="0 0 40 72" aria-hidden="true">
      <path d="M11 60 L20 72 L29 60Z" fill="var(--band)"/>
      <circle cx="20" cy="20" r="18" fill="var(--accent)"/>
      <circle cx="20" cy="20" r="9" fill="none" stroke="#fff" stroke-width="2"/>
      <path d="M11 20 H29 M20 11 C15 16 15 24 20 29 M20 11 C25 16 25 24 20 29" fill="none" stroke="#fff" stroke-width="1.6"/>
    </svg>
    <a href="mailto:info@danakerr.com">info@danakerr.com</a><br>
    www.<span class="domain">quillbarn</span>.com
  </div>

  <div class="contact contact--place">
    <svg class="contact__icon" width="40" height="72" viewBox="0 0 40 72" aria-hidden="true">
      <path d="M11 60 L20 72 L29 60Z" fill="var(--band)"/>
      <circle cx="20" cy="20" r="18" fill="var(--accent)"/>
      <path d="M20 30 C15 23 14 21 14 18 A6 6 0 0 1 26 18 C26 21 25 23 20 30Z" fill="none" stroke="#fff" stroke-width="2"/>
      <circle cx="20" cy="18" r="2" fill="#fff"/>
    </svg>
    your street address, Box-<br>318, Harbour-4470
  </div>

  <div class="stripe"></div>
</section>

</body>
</html>
```